Stationery Design Project

Hi All,

We need you to design stationary for a new Business and Accounting Advisory Firm. We have already got the logo designed and it is attached. If you could also if possible, match the fonts in your design to that on the logo’s provided.

What we need:
- Business Card
- A4 Letter head
- A4 Folders
- PPT template (Title page and regular page)

And what ever else you want to throw in.

We are in the process of getting the web site designed, however below is a list of websites which we like which will give you an understanding of the style that we are going for.

- plavoni.com
- brightfunnelo.com
- hourquillet.com
- artmarrowly.com

I look forward to your seeing your design.

Hi All,

I have just realised that I forgot that i need to include a Licensed Tallymasters image on the letter head, please find attaced as File 1. Could you please have this image in the bottom left header.

Regards,

Gareth

Industry/Entity Type

Business

Requirements
Must have
• Outputs:
- Documents ready to print
- Generic editable information
- Pdf copies of the documents
- Word version of letterhead

```html
<!DOCTYPE html>
<html lang="en">
<head>
<meta charset="utf-8">
<title>Harlow Partners – Business Card</title>
<link rel="stylesheet" href="https://fonts.googleapis.com/css2?family=Open+Sans:wght@400;600&display=swap">
<style>
  :root {
    --stage: #2a2a2a;
    --paper: #ffffff;
    --brand-blue: #3b7fc4;
    --brand-orange: #f5a623;
    --ink-blue: #3c63ad;
    --url-violet: #4b4fc2;
    --band-start: #3fa3d8;
    --band-end: #3a69b0;
    --on-band: #ffffff;
  }
  * { box-sizing: border-box; margin: 0; padding: 0; }
  html, body {
    width: 1200px; height: 900px; overflow: hidden;
    background: var(--stage);
    font-family: "Open Sans", Arial, sans-serif;
  }
  .sheet {
    width: 1200px; height: 900px;
    display: flex; flex-direction: column;
    align-items: center; justify-content: center; gap: 56px;
  }
  .card {
    position: relative;
    width: 620px; height: 354px;
    background: var(--paper);
    border-radius: 4px;
    overflow: hidden;
  }
  /* Back of card */
  .card-back {
    display: flex; flex-direction: column;
    align-items: center; justify-content: center; gap: 34px;
  }
  .brand-lockup { display: flex; align-items: center; gap: 16px; }
  .brand-dot {
    width: 30px; height: 30px; border-radius: 50%;
    background: var(--brand-orange);
  }
  .brand-name {
    font-weight: 600; font-size: 46px; color: var(--brand-blue);
    letter-spacing: 0.5px;
  }
  .web-address {
    font-weight: 600; font-size: 19px; color: var(--url-violet);
    letter-spacing: 0.3px;
  }
  /* Front of card */
  .card-front .brand-lockup {
    position: absolute; left: 34px; top: 30px; gap: 12px;
  }
  .card-front .brand-dot { width: 22px; height: 22px; }
  .card-front .brand-name { font-size: 30px; }
  .name-band {
    position: absolute; left: 290px; right: 0; top: 118px; height: 112px;
    background: linear-gradient(100deg, var(--band-start), var(--band-end));
    color: var(--on-band);
    padding: 14px 0 0 32px;
  }
  .holder-name { font-size: 36px; font-weight: 400; line-height: 1.1; }
  .holder-role { font-size: 22px; margin: 6px 0 0 92px; }
  .contact {
    position: absolute; left: 34px; bottom: 34px;
    list-style: none; color: var(--ink-blue);
    font-size: 15px; line-height: 1.55;
  }
  .contact .pair span + span { margin-left: 28px; }
</style>
</head>
<body>
  <main class="sheet">
    <section class="card card-back" aria-label="Business card back">
      <div class="brand-lockup">
        <span class="brand-dot"></span>
        <span class="brand-name">Harlow Partners</span>
      </div>
      <p class="web-address">www.harlowpartners.com</p>
    </section>

    <section class="card card-front" aria-label="Business card front">
      <div class="brand-lockup">
        <span class="brand-dot"></span>
        <span class="brand-name">Harlow Partners</span>
      </div>
      <div class="name-band">
        <p class="holder-name">John Doe</p>
        <p class="holder-role">Partner</p>
      </div>
      <ul class="contact">
        <li>1234 Somewhere St. City, State, 12345</li>
        <li class="pair"><span>P: (123) 456-7890</span><span>F: (123) 456-7891</span></li>
        <li>E: johndoe@harlowpartners.com</li>
      </ul>
    </section>
  </main>
</body>
</html>
```